Chauffeur Car Driver Needing a design with/without logo for business cards

I'm a chauffeur car driver in Melbourne Australia. I have an extensive list of personal customers and need to provide a professional business card to new customers.
My business name is 'RivaPlus'.
I offer a personalised service to customer who need a transport alternative to taxis. I don't want it to look too 'upmarket' as i don't want it to seem too expensive or only for special occasions. The majority of my clients are business professionals who use me for airport transfers.
I definitely don't want the card/logo to have an image of a car/road etc. I prefer something abstract. A 'pencil-line'-type font will grab my attention but not absolutely necessary. Not too 'digital' or 'ultra - modern' looking.
I need the card to display the following information
Riva Plus - main logo/text
Chauffeur Cars - sub text
Marco Devilles
0452 918 306
bookings@RivaPlus.example.au
I would like the focus to be on 'RivaPlus' with everything else smaller.
Look forward to seeing ideas!!!!
Target Market(s)
Business Corporate Professionals
Industry/Entity Type
Airport
Requirements
Nice to have
- Pencil line type font
Should not have
- Images of cars, road, tyres, steering wheel etc.

```html
<!DOCTYPE html>
<html lang="en">
<head>
<meta charset="utf-8">
<title>Riva Plus – Business Card</title>
<link rel="stylesheet" href="https://fonts.googleapis.com/css2?family=PT+Serif:wght@400;700&display=swap">
<style>
  :root {
    --page-bg: #1b1b1d;
    --navy-top: #22216f;
    --navy-mid: #1b1a5c;
    --band: #1e1d63;
    --band-line: #2a2977;
    --strip: #12113f;
    --ink-light: #f2f2f7;
    --ink-soft: #d3d4e4;
  }
  * { box-sizing: border-box; margin: 0; padding: 0; }
  html, body {
    width: 977px;
    height: 1200px;
    overflow: hidden;
    background: var(--page-bg);
  }
  .canvas {
    position: relative;
    width: 977px;
    height: 1200px;
  }
  .business-card {
    position: absolute;
    left: 58px;
    top: 336px;
    width: 860px;
    height: 528px;
    background: linear-gradient(180deg, var(--navy-top) 0%, var(--navy-mid) 72%);
    box-shadow: 0 18px 40px rgba(0,0,0,0.55);
    overflow: hidden;
  }
  .brand {
    position: absolute;
    top: 132px;
    left: 0;
    right: 0;
    text-align: center;
  }
  .brand-name {
    font-family: "PT Serif", serif;
    font-weight: 700;
    font-size: 84px;
    line-height: 1;
    color: var(--ink-light);
  }
  .brand-tagline {
    margin-top: 14px;
    font-family: "PT Serif", serif;
    font-weight: 400;
    font-size: 28px;
    color: var(--ink-soft);
  }
  .contact-band {
    position: absolute;
    left: 0;
    right: 0;
    top: 382px;
    height: 108px;
    background: var(--band);
    border-top: 1px solid var(--band-line);
    display: flex;
    flex-direction: column;
    align-items: center;
    justify-content: center;
    gap: 4px;
  }
  .contact-name {
    font-family: "PT Serif", serif;
    font-weight: 700;
    font-size: 27px;
    color: var(--ink-light);
  }
  .contact-details {
    font-family: "PT Serif", serif;
    font-weight: 400;
    font-size: 25px;
    color: var(--ink-soft);
  }
  .contact-details .divider { padding: 0 6px; }
  .base-strip {
    position: absolute;
    left: 0;
    right: 0;
    bottom: 0;
    height: 38px;
    background: var(--strip);
  }
</style>
</head>
<body>
  <main class="canvas">
    <section class="business-card">
      <div class="brand">
        <div class="brand-name">Riva Plus</div>
        <div class="brand-tagline">Chauffeur Cars</div>
      </div>
      <div class="contact-band">
        <div class="contact-name">Marco Devilles</div>
        <div class="contact-details">0452 918 306<span class="divider">|</span>bookings@RivaPlus.example.au</div>
      </div>
      <div class="base-strip"></div>
    </section>
  </main>
</body>
</html>
```